Electrical Contracting business card design

We need a simple business card design for an Electrical Contracting business. A simple design would be appreciated
This company has 2 directors so on one it would have Dale Morrow & another with Shane Morrow.
Updates

Project Deadline Extended
Reason: Hello A few designers have asked for a logo unfortunately we don't have one so have extended deadline to see who can help us out with this. CHEERS

Project Deadline Extended
Reason: Waiting for business partner to return from xmas break. cheers

Industry/Entity Type

Business

Contact Information for Business Card

Quolvin Electrical Services P/L
REC: 63417
Residential Commercial Industrial
Service-Repairs-Renovations-Installations-Telephone-Data
Dale Morrow-Ph: 0437 612 388
Email: dale@quolvinelectrical.com.au

Requirements
Should not have
• The design should not have any electrical appliances in it ie: power-points, leads, houses etc.

```html
<!DOCTYPE html>
<html lang="en">
<head>
<meta charset="utf-8">
<title>Quolvin Electrical Services – Business Card</title>
<link rel="stylesheet" href="https://fonts.googleapis.com/css2?family=Oswald:wght@500&family=Roboto+Condensed:wght@400;700&display=swap">
<style>
  :root {
    --page-bg: #2b3838;
    --card-white: #ffffff;
    --brand-blue: #1d4b8f;
    --photo-deep: #2a1f8c;
    --photo-mid: #3b5fc4;
    --photo-light: #38b6d8;
    --ink: #2a2a2a;
    --ink-soft: #555555;
  }
  html, body {
    margin: 0;
    width: 1200px;
    height: 1000px;
    overflow: hidden;
    background: var(--page-bg);
  }
  .canvas {
    position: relative;
    width: 1200px;
    height: 1000px;
  }
  .card {
    position: absolute;
    left: 250px;
    width: 700px;
    height: 400px;
    box-shadow: 0 10px 30px rgba(0,0,0,0.45);
    overflow: hidden;
  }
  .card--front { top: 60px; background: var(--card-white); }
  .card--back  { top: 540px; background: var(--brand-blue); }

  .photo-row {
    position: absolute;
    left: 0;
    display: flex;
    gap: 8px;
  }
  .photo-row--top { top: 0; left: 36px; width: 630px; height: 58px; }
  .photo-row--mid { top: 168px; left: 150px; width: 516px; height: 104px; }
  .photo-tile {
    flex: 1;
    background: linear-gradient(135deg, var(--photo-deep), var(--photo-mid) 55%, var(--photo-light));
  }

  .brand {
    position: absolute;
    display: flex;
    align-items: center;
    gap: 14px;
    font-family: "Oswald", sans-serif;
    font-weight: 500;
    text-transform: uppercase;
    letter-spacing: 0.5px;
  }
  .brand__mark { width: 40px; height: 40px; flex: none; }
  .card--front .brand { top: 92px; left: 36px; color: var(--ink); font-size: 34px; }
  .card--front .brand__mark { background: var(--brand-blue); }

  .person {
    position: absolute;
    top: 86px;
    right: 34px;
    text-align: right;
    font-family: "Oswald", sans-serif;
    font-weight: 500;
    text-transform: uppercase;
    color: var(--ink);
  }
  .person__name { font-size: 24px; line-height: 1.1; }
  .person__role { font-size: 12px; letter-spacing: 1px; color: var(--ink-soft); }

  .contact {
    position: absolute;
    left: 150px;
    right: 34px;
    top: 292px;
    text-align: center;
    font-family: "Roboto Condensed", sans-serif;
    font-size: 17px;
    line-height: 1.35;
    color: var(--ink);
  }
  .contact__line--strong { font-weight: 700; }

  .card--back .brand {
    top: 50%;
    left: 50%;
    transform: translate(-50%, -50%);
    color: var(--card-white);
    font-size: 40px;
    white-space: nowrap;
  }
  .card--back .brand__mark { background: var(--card-white); width: 46px; height: 46px; }
</style>
</head>
<body>
<main class="canvas">
  <section class="card card--front" aria-label="Business card front">
    <div class="photo-row photo-row--top">
      <div class="photo-tile" role="img" aria-label="Blue-toned close-up photo of a circuit board"></div>
      <div class="photo-tile" role="img" aria-label="Blue-toned close-up photo of a circuit board"></div>
      <div class="photo-tile" role="img" aria-label="Blue-toned close-up photo of a circuit board"></div>
    </div>

    <div class="brand">
      <span class="brand__mark"></span>
      <span class="brand__name">Quolvin Electrical Services</span>
    </div>

    <div class="person">
      <div class="person__name">Dale Morrow</div>
      <div class="person__role">Director</div>
    </div>

    <div class="photo-row photo-row--mid">
      <div class="photo-tile" role="img" aria-label="Blue-toned close-up photo of circuit components"></div>
      <div class="photo-tile" role="img" aria-label="Blue-toned close-up photo of circuit components"></div>
      <div class="photo-tile" role="img" aria-label="Blue-toned close-up photo of circuit components"></div>
      <div class="photo-tile" role="img" aria-label="Blue-toned close-up photo of circuit components"></div>
    </div>

    <div class="contact">
      <div class="contact__line">Quolvin Electrical Services P/L REC :</div>
      <div class="contact__line">63417 Residential Commercial Industrial Service</div>
      <div class="contact__line">- Repairs - Renovations - Installations</div>
      <div class="contact__line contact__line--strong">Ph: 0437 612 388 &nbsp;Email: dale@quolvinelectrical.com.au</div>
    </div>
  </section>

  <section class="card card--back" aria-label="Business card back">
    <div class="brand">
      <span class="brand__mark"></span>
      <span class="brand__name">Quolvin Electrical Services</span>
    </div>
  </section>
</main>
</body>
</html>
```